TRV Construction and Remodeling

Prefer a matte black card with some colors that pop, but subtle. Contact info. Show General Contractor professional way. Can you please remove renovations repairs maintenance off of my logo.

Target Market(s)

Property and business investors. Homeowners

Industry/Entity Type

Construction

Contact Information for Business Card

Name: Dorian Vekkart, Title: CEO, Phone: 555-014-7392, Email: Dorian@TRVbuildNkx.example, website: www TRVbuildNkx.example

• Designer choose

Colors

Designer to choose colors to be used in the design.

Requirements
Must have
• Uniqueness. Double sided since it wont let me choose that. Professional look, be eye catching and catchy. QR code to my website
Nice to have
• Matte black background, subtle bright colors that pop, but I am open to anything. I also like black and gold with some red. Possible Harborton Ravens logo colored stars somewhere around the logo or on the back. Just to rep my city
Should not have
• pink. Something you would see somewhere else. gif pictures or generated pictures.

```html
<!DOCTYPE html>
<html lang="en">
<head>
<meta charset="utf-8">
<title>TRV Construction and Remodeling — Business Card</title>
<link href="https://fonts.googleapis.com/css2?family=Michroma&display=swap" rel="stylesheet">
<style>
  :root {
    --backdrop: #a9a9a9;
    --card: #232323;
    --ink: #ffffff;
    --accent-red: #e0212a;
    --faint-red: #3a2224;
    --gold: #cfa93e;
    --qr-field: #f2f2f2;
  }
  * { margin: 0; padding: 0; box-sizing: border-box; }
  html, body {
    width: 1200px; height: 800px; overflow: hidden;
    background: var(--backdrop);
    font-family: "Michroma", "Arial", sans-serif;
  }
  .stage {
    width: 1200px; height: 800px;
    display: flex; align-items: center; justify-content: center; gap: 40px;
  }
  .card {
    position: relative;
    width: 540px; height: 309px;
    background: var(--card);
    overflow: hidden;
    box-shadow: 0 10px 30px rgba(0,0,0,0.25);
  }

  /* Front */
  .front-decoration {
    position: absolute; left: 0; bottom: 9px;
    width: 170px; height: 180px;
    background: linear-gradient(160deg, rgba(58,34,36,0) 0%, var(--faint-red) 70%);
  }
  .front-brand {
    position: absolute; top: 40px; right: 40px;
    display: flex; align-items: center; gap: 10px;
    color: var(--ink); font-size: 16px; letter-spacing: 0.3px;
    white-space: nowrap;
  }
  .brand-square {
    flex: 0 0 auto;
    width: 14px; height: 14px; border: 2px solid var(--accent-red);
  }
  .person {
    position: absolute; left: 40px; top: 146px;
  }
  .person-name {
    color: var(--accent-red); font-size: 19px; text-transform: uppercase; letter-spacing: 0.2px;
    white-space: nowrap;
  }
  .person-title {
    color: var(--ink); font-size: 11px; margin-top: 8px;
  }
  .divider {
    position: absolute; left: 40px; right: 40px; top: 206px;
    height: 1px; background: var(--accent-red);
  }
  .contact-list {
    position: absolute; left: 40px; top: 220px;
    list-style: none; color: var(--ink); font-size: 11px;
  }
  .contact-list li { display: flex; align-items: center; gap: 8px; margin-bottom: 8px; white-space: nowrap; }
  .contact-list svg { width: 11px; height: 11px; fill: var(--accent-red); flex: 0 0 auto; }
  .website {
    position: absolute; right: 40px; bottom: 24px;
    color: var(--ink); font-size: 10px; white-space: nowrap;
  }
  .edge-band {
    position: absolute; left: 0; right: 0; bottom: 0; height: 9px;
    display: flex;
  }
  .edge-band .band-red { flex: 0 0 62%; background: var(--accent-red); }
  .edge-band .band-white { flex: 1; background: var(--ink); }

  /* Back */
  .back-brand {
    position: absolute; left: 0; right: 0; top: 50%;
    transform: translateY(-50%);
    color: var(--gold); font-size: 26px; letter-spacing: 0.5px; text-align: center;
    line-height: 1.45;
  }
  .qr-code {
    position: absolute; right: 24px; bottom: 24px;
    width: 64px; height: 64px;
    background: var(--qr-field);
    border: 3px solid var(--gold);
  }
</style>
</head>
<body>
<main class="stage">
  <section class="card card-front" aria-label="Business card front">
    <div class="front-decoration" role="img" aria-label="Faint utility pole and house outline decoration in dark red"></div>
    <div class="front-brand">
      <span class="brand-square"></span>
      <span class="brand-name">TRV Construction &amp; Remodeling</span>
    </div>
    <div class="person">
      <p class="person-name">Dorian Vekkart</p>
      <p class="person-title">CEO</p>
    </div>
    <div class="divider"></div>
    <ul class="contact-list">
      <li>
        <svg viewBox="0 0 24 24" aria-hidden="true"><path d="M6.6 10.8c1.4 2.8 3.8 5.1 6.6 6.6l2.2-2.2c.3-.3.7-.4 1-.2 1.1.4 2.3.6 3.6.6.6 0 1 .4 1 1V20c0 .6-.4 1-1 1C10.6 21 3 13.4 3 4c0-.6.4-1 1-1h3.5c.6 0 1 .4 1 1 0 1.3.2 2.5.6 3.6.1.3 0 .7-.2 1L6.6 10.8z"/></svg>
        555-014-7392
      </li>
      <li>
        <svg viewBox="0 0 24 24" aria-hidden="true"><path d="M2 5h20v14H2V5zm2 2v.5l8 5 8-5V7H4zm0 2.8V17h16V9.8l-8 5-8-5z"/></svg>
        Dorian@TRVbuildNkx.example
      </li>
    </ul>
    <p class="website">www TRVbuildNkx.example</p>
    <div class="edge-band"><span class="band-red"></span><span class="band-white"></span></div>
  </section>

  <section class="card card-back" aria-label="Business card back">
    <p class="back-brand">TRV Construction<br>&amp; Remodeling</p>
    <div class="qr-code" role="img" aria-label="QR code linking to www TRVbuildNkx.example"></div>
  </section>
</main>
</body>
</html>
```